About the book: It is an A5 size book, small 40 pages miniguide
Book title: The pocket handbook of housing loans
Book subtitle: The quiet road to plenty
Author: Tod Brisbane
Back cover content: Please see attached word document "back page"
Colours: Our company logo should go at the back of the book. One colour we can't use is red. As this is a finance book the red colour is seen negatively. may be light green? you are the expert.
I think lots of white space will work well.
NOTE: please read the back cover notes to get an understanding of what the book is about. It educates readers about finance in property investing. It makes sense that image used combines 'property' and 'finance'. please read back page document attached.
NOTE: it is a small A5 , 40 page book . Its a miniguide rather than a book .
Updates

Project Deadline Extended
Reason: Dear designers, Thank you for submitting your work over the last few days. Unfortunately we haven't been able to get back to you regarding the final selection of design as the Author of the book has been away on leave with his family without reliable internet access. He is now back and will be giving feedback as we go. We apologise for the time extension. Unfortunately the site didn’t allow me to limit the extension for less than 5 days but we may not require that long. Thanks again. Lulu

Project Deadline Extended
Reason: We apologies we hadn't finalized a decision on this project due to the person from our end being away. We would like to finalise this design as soon as possible.

Target Market(s)

22 - 45 age group. Most fall between 30-40. Both male and female. couples , individuals etc ...

Industry/Entity Type

Finance

Font styles to use
Other font styles liked:
• sabon/Aeriel. Let me know if any other suggestions.

Requirements
Nice to have
• use green colour if possible but not essential.

```html
<!DOCTYPE html>
<html lang="en">
<head>
<meta charset="utf-8">
<title>The Pocket Handbook of Housing Loans — Cover</title>
<link rel="stylesheet" href="https://fonts.googleapis.com/css2?family=Cinzel:wght@500&family=Open+Sans:wght@600;700&family=Oswald:wght@500&display=swap">
<style>
  :root {
    --band-green: #3b9b34;
    --heading-green: #3f9a2f;
    --ink-blue: #2c4096;
    --title-blue: #33489b;
    --paper: #ffffff;
    --white: #ffffff;
  }
  * { margin: 0; padding: 0; box-sizing: border-box; }
  html, body { width: 1200px; height: 845px; overflow: hidden; background: var(--paper); }
  .cover { position: relative; width: 1200px; height: 845px; overflow: hidden; background: var(--paper); font-family: "Open Sans", Arial, sans-serif; }

  .band { position: absolute; left: 0; width: 1200px; background: var(--band-green); }
  .band--top { top: 0; height: 82px; }
  .band--bottom { top: 765px; height: 80px; }

  .author {
    position: absolute; top: 22px; left: 745px;
    font-family: "Cinzel", Georgia, serif; font-weight: 500;
    font-size: 32px; letter-spacing: 3px; color: var(--white);
  }

  /* Back cover */
  .back { position: absolute; left: 42px; top: 115px; width: 525px; color: var(--ink-blue); }
  .back__title { text-align: center; color: var(--heading-green); font-size: 17px; font-weight: 700; width: 500px; }
  .back__subtitle { text-align: center; font-size: 18px; font-weight: 700; margin-top: 9px; width: 500px; }
  .back__body { margin-top: 16px; font-size: 11.5px; letter-spacing: -0.2px; font-weight: 700; line-height: 17.5px; }
  .back__body p + p { margin-top: 17.5px; }
  .lessons { list-style: none; margin-top: 17.5px; }
  .lessons li { font-size: 11.5px; letter-spacing: -0.2px; font-weight: 700; line-height: 17.5px; }
  .lessons li::before { content: "•"; color: var(--heading-green); margin-right: 6px; }
  .lessons li.gap { margin-top: 17.5px; }

  .publisher { position: absolute; left: 183px; top: 672px; display: flex; flex-direction: column; gap: 8px; }
  .publisher__name { display: flex; align-items: center; gap: 8px; font-size: 20px; font-weight: 700; color: var(--ink-blue); }
  .publisher__mark { width: 14px; height: 14px; background: var(--band-green); }
  .publisher__tagline { font-size: 10.5px; font-weight: 600; color: #333; border-top: 1px solid #333; padding-top: 4px; }

  /* Front cover */
  .artwork { position: absolute; left: 670px; top: 82px; width: 500px; height: 510px; }
  .title {
    position: absolute; right: 43px; top: 608px;
    font-family: "Oswald", "Arial Narrow", sans-serif; font-weight: 500;
    font-size: 54px; line-height: 66px; color: var(--title-blue);
    text-transform: uppercase; text-align: right; white-space: nowrap;
  }
  .subtitle {
    position: absolute; left: 716px; top: 788px;
    font-size: 22px; font-weight: 700; letter-spacing: 0.5px; color: var(--white); text-transform: uppercase;
  }
</style>
</head>
<body>
<main class="cover">
  <div class="band band--top"></div>
  <div class="band band--bottom"></div>

  <p class="author">Tod Brisbane</p>

  <section class="back">
    <h2 class="back__title">THE POCKET HANDBOOK OF HOUSING LOANS.</h2>
    <p class="back__subtitle">The quiet road to plenty.</p>
    <div class="back__body">
      <p>The number-one reason most investors never own more than one property is finance.<br>
      For them, getting and managing money is the scariest part of investing.<br>
      You must be 100% informed when structuring your loans. Before you even think about finding a property, you must understand the valuation process.</p>
      <p>In simple, jargon-free language, this pocket handbook arms you with a wealth of knowledge to reduce risk and keep control of your investment goals.<br>
      Its many vital lessons include:</p>
    </div>
    <ul class="lessons">
      <li>How to keep your own home safe and out of the bank’s hands.</li>
      <li>The first step to successful investing is knowing where you want to finish. Learn how different exit strategies affect your investment plan.</li>
      <li class="gap">The main reason most Australians aren’t wealthy is that they don’t know the difference between appreciating and depreciating assets and beneficial and non-beneficial liabilities. Learn to view everything as one or the other.</li>
      <li class="gap">Grasping the concept of leverage and other people’s money will dramatically increase your return on equity.</li>
      <li class="gap">Banking and finance. By knowing what lenders need to asses a loan, you can apply with confidence and put yourself ahead of the pack.</li>
    </ul>
  </section>

  <div class="publisher">
    <span class="publisher__name"><span class="publisher__mark"></span>Fairholm Wealth Partners</span>
    <span class="publisher__tagline">Growing wealth through property ownership</span>
  </div>

  <svg class="artwork" role="img" aria-label="Illustration of a small house built from banknotes with notes flying upward above it" viewBox="0 0 500 510">
    <defs>
      <radialGradient id="artwork-tone" cx="50%" cy="65%" r="60%">
        <stop offset="0%" stop-color="#9fb78f"/>
        <stop offset="55%" stop-color="#d3dfca"/>
        <stop offset="100%" stop-color="#ffffff"/>
      </radialGradient>
    </defs>
    <rect width="500" height="510" fill="url(#artwork-tone)"/>
  </svg>

  <h1 class="title">The Pocket Handbook<br>of Housing Loans</h1>
  <p class="subtitle">The quiet road to plenty</p>
</main>
</body>
</html>
```